Tradeshow Banner Design (Qty2, 6'H x 2'W)

Brightline Works is an Electrical, Fire Alarm, and Security Contracting company. For tradeshows, we would like 2 vertical Banners to put behind our booth. Our colors are Red, Grey & Black. I would like the Banners to be informative on what services we provide, with some appealing Graphic Design. (bwk-qtr.com)
Slogan: Safeguarding Communities Electrical, Fire & Security Solutions
Target Market(s)
Commercial Construction Clients
Industry/Entity Type
Electrical / Construction
Font styles to use
Other font styles liked:
- Aileron
Colors
EB3D1F
EC4F4E
F09395
F8D3D4
FCEDEE
Requirements
Must have
- Our Logo, Color Scheme, Brief Caption of the services we provide
Nice to have
- Appealing Imagery & a modern/simplistic design

```html
<!DOCTYPE html>
<html lang="en">
<head>
<meta charset="utf-8">
<title>Brightline Works – Tradeshow Banners</title>
<link rel="stylesheet" href="https://fonts.googleapis.com/css2?family=Roboto+Condensed:wght@500&family=Roboto:wght@300;400&display=swap">
<style>
  :root {
    --brand-red: #ec1c26;
    --brand-grey: #dcdcdd;
    --salmon: #f2757a;
    --blush: #f8d0d2;
    --text-grey: #858585;
    --ring-shadow: #a9a9a9;
    --page: #f4f4f5;
    --white: #ffffff;
  }
  * { margin: 0; padding: 0; box-sizing: border-box; }
  html, body { width: 1200px; height: 1200px; overflow: hidden; background: var(--page); }
  .stage { position: relative; width: 1200px; height: 1200px; }

  .banner { position: absolute; width: 396px; overflow: hidden; }
  .banner--red-top { left: 172px; top: 101px; height: 1000px; }
  .banner--grey-top { left: 640px; top: 96px; height: 1004px; }
  .banner__art { position: absolute; inset: 0; width: 100%; height: 100%; display: block; }

  .wordmark {
    position: absolute; left: 0; width: 100%; text-align: center;
    font-family: "Roboto Condensed", "Arial Narrow", sans-serif;
    font-weight: 500; font-size: 62px; line-height: 58px; letter-spacing: -1px;
  }
  .tagline {
    position: absolute; left: 0; width: 100%; text-align: center;
    font-family: "Roboto", Arial, sans-serif; font-weight: 300;
    font-size: 19px; letter-spacing: 1.2px; white-space: nowrap;
  }
  .tagline .divider { display: inline-block; width: 1.5px; height: 20px; background: currentColor; vertical-align: -3px; margin: 0 4px; }

  .on-red { color: var(--brand-grey); }
  .on-grey-red { color: var(--brand-red); }
  .on-grey-muted { color: var(--text-grey); }

  .follow {
    position: absolute; left: 0; width: 100%; text-align: center;
    font-family: "Roboto", Arial, sans-serif; font-weight: 400; font-size: 13px;
  }
  .social-row { position: absolute; left: 0; width: 100%; display: flex; justify-content: center; gap: 8px; }
  .social-slot { width: 30px; height: 30px; border-radius: 5px; }
  .social-slot--grey { background: var(--text-grey); }
  .social-slot--light { background: var(--brand-grey); }
</style>
</head>
<body>
<main class="stage">

  <!-- Banner A: red header, grey body -->
  <section class="banner banner--red-top">
    <svg class="banner__art" viewBox="0 0 638 1610" preserveAspectRatio="none">
      <rect width="638" height="1610" fill="var(--brand-grey)"/>
      <polygon points="0,510 638,565 638,698 0,740" fill="var(--blush)"/>
      <polygon points="0,510 90,536 90,660 0,568" fill="var(--salmon)"/>
      <polygon points="0,0 638,0 638,565 0,510" fill="var(--brand-red)"/>
      <polygon points="0,1463 455,1610 75,1610 0,1520" fill="var(--salmon)"/>
      <polygon points="638,1510 638,1610 455,1610" fill="var(--blush)"/>
      <circle cx="320" cy="622" r="250" fill="var(--ring-shadow)"/>
      <circle cx="320" cy="606" r="240" fill="var(--white)"/>
      <circle cx="320" cy="606" r="228" fill="var(--brand-red)" role="img" aria-label="Flame emblem"/>
    </svg>

    <div class="wordmark on-red" style="top:34px">BRIGHTLINE<br>WORKS</div>
    <div class="tagline on-red" style="top:157px">ELECTRICAL<span class="divider"></span>FIRE<span class="divider"></span>SECURITY</div>

    <div class="wordmark on-grey-muted" style="top:590px">BRIGHTLINE<br>WORKS</div>
    <div class="tagline on-grey-muted" style="top:707px">ELECTRICAL<span class="divider"></span>FIRE<span class="divider"></span>SECURITY</div>

    <div class="follow on-grey-muted" style="top:862px">follow us</div>
    <div class="social-row" style="top:885px">
      <span class="social-slot social-slot--grey"></span>
      <span class="social-slot social-slot--grey"></span>
      <span class="social-slot social-slot--grey"></span>
      <span class="social-slot social-slot--grey"></span>
    </div>
  </section>

  <!-- Banner B: grey header, red footer -->
  <section class="banner banner--grey-top">
    <svg class="banner__art" viewBox="0 0 638 1617" preserveAspectRatio="none">
      <rect width="638" height="1617" fill="var(--brand-grey)"/>
      <polygon points="0,971 433,875 638,934 638,1617 0,1617" fill="var(--blush)"/>
      <polygon points="0,1108 433,875 638,1164 638,1617 0,1617" fill="var(--brand-red)"/>
      <polygon points="433,875 638,1104 638,1164 175,1018" fill="var(--salmon)"/>
      <polygon points="433,875 638,934 638,1104" fill="var(--blush)"/>
      <circle cx="319" cy="630" r="250" fill="var(--ring-shadow)"/>
      <circle cx="319" cy="614" r="240" fill="var(--white)"/>
      <circle cx="319" cy="614" r="228" fill="var(--brand-red)" role="img" aria-label="Flame emblem"/>
    </svg>

    <div class="wordmark on-grey-red" style="top:39px">BRIGHTLINE<br>WORKS</div>
    <div class="tagline on-grey-red" style="top:162px">ELECTRICAL<span class="divider"></span>FIRE<span class="divider"></span>SECURITY</div>

    <div class="follow on-red" style="top:734px">follow us</div>
    <div class="social-row" style="top:757px">
      <span class="social-slot social-slot--light"></span>
      <span class="social-slot social-slot--light"></span>
      <span class="social-slot social-slot--light"></span>
      <span class="social-slot social-slot--light"></span>
    </div>

    <div class="wordmark on-red" style="top:815px">BRIGHTLINE<br>WORKS</div>
    <div class="tagline on-red" style="top:938px">ELECTRICAL<span class="divider"></span>FIRE<span class="divider"></span>SECURITY</div>
  </section>

</main>
</body>
</html>
```